Taking a Paper and turning into a wonderful White Paper for Prospects and Clients

This is a white paper I need designed. I am including my company brochure so you can see the design/fonts being used and I'm including a white paper created - one that I like very much.

I am "NOT" looking for a cookie cutter white paper. I'm looking for a nice, clean design but with some creativity. Check out the white paper I included and you will get the idea.

Also included:
- the paper to be designed
- the paper to be designed "WITH" suggested design features such as carve outs, call outs and such

A few things I "DO NOT" like:
- images that are cheesy or corny
* people sitting at a table in a meeting
* Buildings

The white paper I included did not use pictures but had more design created by the firm. I like this approach and will probably give something like this more weight but is not required.
Updates

Reason: Realized time frame was too tight

Target Market(s)

Higher-End, wealthier clients

Industry/Entity Type

It Company

Requirements
Must have
• I DO NOT want the copy to be bunched together. The layout should flow where the copy is broken in the right spots to make reading easier. If you read a paper and it is just copy, interest is lost by everyone.
• COLORS: you can see from what I have included the colors I use
• My preference are very balanced colors using "clean spacing"

```html
<!DOCTYPE html>
<html lang="en">
<head>
<meta charset="utf-8">
<title>Veranto White Paper – Spread</title>
<link rel="stylesheet" href="https://fonts.googleapis.com/css2?family=Josefin+Sans:wght@600;700&family=Raleway:wght@300;400&family=Alegreya+Sans:wght@700&display=swap">
<style>
  :root {
    --canvas: #ffffff;
    --page: #ffffff;
    --ink-deep: #1e3846;
    --ink-teal: #24505e;
    --ink-muted: #9eaeaa;
    --body-text: #4a4a4a;
    --rule: #2c4c5a;
    --shadow: rgba(0, 0, 0, 0.28);
  }
  * { margin: 0; padding: 0; box-sizing: border-box; }
  html, body {
    width: 1200px; height: 520px; overflow: hidden;
    background: var(--canvas);
  }
  .spread { position: relative; width: 1200px; height: 520px; }
  .page {
    position: absolute; top: 22px; width: 368px; height: 474px;
    background: var(--page);
    box-shadow: 2px 3px 8px var(--shadow);
  }
  .page--intro { left: 14px; }
  .page--steps { left: 406px; }
  .page--oversight { left: 805px; }

  .brand {
    position: absolute; left: 24px; top: 24px;
    display: flex; align-items: center; gap: 3px;
    font-family: "Josefin Sans", sans-serif; font-weight: 700;
    font-size: 6px; letter-spacing: 0.8px; color: var(--ink-teal);
  }
  .brand-dot { width: 3px; height: 3px; border-radius: 50%; background: var(--ink-teal); }

  .body-copy, .item-text, .answer p {
    font-family: "Raleway", sans-serif; font-weight: 300;
    font-size: 7.4px; line-height: 12px; color: var(--body-text);
  }
  .body-copy { position: absolute; left: 48px; width: 262px; }

  .chevron { position: absolute; width: 5px; height: 7px; }

  .callout {
    position: absolute; left: 107px; top: 117px; width: 230px;
    font-family: "Alegreya Sans", sans-serif; font-weight: 700;
    font-size: 15px; line-height: 19px; color: var(--ink-deep);
  }

  .col-heading {
    position: absolute; top: 60px;
    font-family: "Josefin Sans", sans-serif; font-weight: 700;
    font-size: 13.5px; line-height: 16.5px; letter-spacing: 0.2px;
    text-transform: uppercase;
  }
  .col-heading--problem { left: 63px; color: var(--ink-deep); }
  .col-heading--steps { left: 169px; color: var(--ink-teal); }
  .page--oversight .col-heading { color: var(--ink-muted); }

  .divider {
    position: absolute; left: 151px; top: 58px; width: 1.4px; height: 360px;
    background: var(--rule);
  }
  .item-text { position: absolute; left: 63px; width: 76px; }
  .page--oversight .item-text { text-align: justify; }
  .answer { position: absolute; left: 169px; width: 164px; }
  .answer p { position: absolute; left: 0; width: 164px; }
</style>
</head>
<body>
<main class="spread">

  <!-- Page: introduction -->
  <section class="page page--intro">
    <div class="brand"><span>VERANTO</span><span class="brand-dot"></span></div>
    <p class="body-copy" style="top:60px">The fine points in the differences between “the fiduciary standard” and “the suitability standard” are important for all of us to know, to be sure, but what’s most important for now is to understand that</p>
    <svg class="chevron" style="left:74px;top:124px" viewBox="0 0 5 7"><path d="M1 0.8 L4 3.5 L1 6.2" fill="none" stroke="#1e3846" stroke-width="1.4"/></svg>
    <p class="callout">the mere fact of an adviser being a fiduciary does not guarantee that the adviser will do the right things for you.</p>
    <p class="body-copy" style="top:210px">After all, on the surface, Dev Rathore seemed like a trustworthy professional. He said he was a Certified Public Accountant. He worked through Halvern Wealth Advisers. He was endorsed by the National Athletes Guild. And he regularly attended the same church as Cole Brennan. Had you asked him “Are you a fiduciary?” he would have said “Yes.”</p>
    <p class="body-copy" style="top:284px">Veranto understands the daunting challenges investors face in trying to verify that their current, or potential future financial advisers are trustworthy. Our deep, broad knowledge of the field allowed us to develop our world-class system for auditing your financial advisors. Here is a sampling of the steps we would have taken, had Cole Brennan been our client:</p>
  </section>

  <!-- Page: credentials and funds -->
  <section class="page page--steps">
    <div class="brand"><span>VERANTO</span><span class="brand-dot"></span></div>
    <h2 class="col-heading col-heading--problem">Problem<br>with<br>Rathore</h2>
    <h2 class="col-heading col-heading--steps">Veranto’s<br>steps to<br>protect you</h2>
    <div class="divider"></div>

    <svg class="chevron" style="left:42px;top:136px" viewBox="0 0 5 7"><path d="M1 0.8 L4 3.5 L1 6.2" fill="none" stroke="#1e3846" stroke-width="1.4"/></svg>
    <p class="item-text" style="top:133px">Rathore misrepresented himself as a CPA, but was not one.</p>
    <svg class="chevron" style="left:42px;top:220px" viewBox="0 0 5 7"><path d="M1 0.8 L4 3.5 L1 6.2" fill="none" stroke="#1e3846" stroke-width="1.4"/></svg>
    <p class="item-text" style="top:217px">Rathore improperly diverted Brennan’s funds.</p>

    <div class="answer" style="top:0">
      <p style="top:130px">We perform thoroughgoing background checks for every single credential an advisor claims.</p>
      <p style="top:165px">We thoroughly verify claims about both educational background and professional certifications.</p>
      <p style="top:222px">We obtain your account statements showing assets held, and any transfers.</p>
      <p style="top:256px">In Brennan’s case, we would have seen the transfers to The Seat Exchange, and then verified with Brennan that he had authorized those transfers for the reported amounts.</p>
      <p style="top:314px">Additionally, when an advisor makes outside investments for our clients, we do deeper dives.</p>
      <p style="top:350px">Why was the investment bought? Who has control of the investment? How are the assets valued and audited?</p>
      <p style="top:396px">We answer those kinds of questions. We can clearly explain to you why we posed each question and what we think of the answer.</p>
    </div>
  </section>

  <!-- Page: oversight and endorsements -->
  <section class="page page--oversight">
    <div class="brand"><span>VERANTO</span><span class="brand-dot"></span></div>
    <h2 class="col-heading col-heading--problem">Problem<br>with<br>Rathore</h2>
    <h2 class="col-heading col-heading--steps">Veranto’s<br>steps to<br>protect you</h2>
    <div class="divider"></div>

    <svg class="chevron" style="left:42px;top:135px" viewBox="0 0 5 7"><path d="M1 0.8 L4 3.5 L1 6.2" fill="none" stroke="#1e3846" stroke-width="1.4"/></svg>
    <p class="item-text" style="top:132px">Rathore’s superiors at Halvern Capital failed to provide adequate ethical oversight of his work</p>
    <svg class="chevron" style="left:42px;top:222px" viewBox="0 0 5 7"><path d="M1 0.8 L4 3.5 L1 6.2" fill="none" stroke="#1e3846" stroke-width="1.4"/></svg>
    <p class="item-text" style="top:210px">Rathore was endorsed by the National Athletes Guild</p>

    <div class="answer" style="top:0">
      <p style="top:130px">We would have been evaluating how Halvern Capital’s management structure provides oversight and auditing of what its advisors are doing for their clients.</p>
      <p style="top:210px">Whatever the source of such an endorsement – be it a players’ association, a listing in the Market Ledger Top 400, or Capital Digest Top 100 Advisors, etc. -- we view it with great skepticism.</p>
      <p style="top:267px">Why?</p>
      <p style="top:299px">These organizations base their advisor rankings on limited metrics such as the number of years an advisor has been in the industry and the types of clients the advisor has.</p>
      <p style="top:345px">Those metrics are of small import for an individual investor. Such limited metrics comprise less than 10% of what Veranto looks at when evaluating financial advisors.</p>
    </div>
  </section>

</main>
</body>
</html>
```